Coffee bag and coffee beer revamp

We need a coffee bag design where we can print two stickers and they fit nicely on the bag. this is an example of 500gr bag. We will also need 250gr and 1kilo versions.

One the logo attached and the other the coffee description details attached.
This should sit nicely on the white bag example attached.
One is also a photo of what we have but it needed some work to make sure dimensions are good and its clear.
Example: attached of text and these will be variable values that we need the label to edit and they should be different colour labels - we have 6 types of coffee.

<COFFEE TYPE> example House BLEND
<DATE ROASTED> 17/03/23
Text always the same -- "Consume within 12 months"

I have also attache the font and original files. There can be some colour added.

Other types of coffee

SIDAMO
GUATEMALA
SANTOS
COSTA RICA
SUPREMO
DECAF

The beer is just the logo and text "Delvana Cold Brew Coffee" label with the date and logo.

Target Market(s)

coffee lovers

Industry/Entity Type

food

Font styles to use
Other font styles liked:
• i will upload the fonts

Colors
EB3D1F
EC4F4E
F09395
F8D3D4
FCEDEE

Requirements
Nice to have
• can try alternative colour? even just for labels

```html
<!DOCTYPE html>
<html lang="en">
<head>
<meta charset="utf-8">
<title>Delvana Coffee – House Blend bag labels</title>
<link rel="stylesheet" href="https://fonts.googleapis.com/css2?family=Josefin+Sans:wght@400;600;700&family=Quicksand:wght@400;500;600&display=swap">
<style>
  :root {
    --red: #c41d36;
    --red-soft: #f8d3d4;
    --ink: #2a2a2a;
    --paper: #ffffff;
    --backdrop: #e6e6e6;
    --grey-line: #555555;
  }
  * { box-sizing: border-box; margin: 0; padding: 0; }
  html, body { width: 898px; height: 1200px; overflow: hidden; }
  body {
    background: var(--backdrop);
    font-family: "Quicksand", sans-serif;
    color: var(--ink);
    position: relative;
  }
  .bag-face {
    position: absolute;
    top: 330px;
    width: 400px;
    height: 540px;
    background: var(--paper);
  }
  .bag-front { left: 32px; }
  .bag-back { left: 466px; }

  /* front */
  .blend-band {
    position: absolute; top: 70px; left: 0; right: 0; height: 76px;
    background: var(--red);
    display: flex; align-items: center; justify-content: center;
  }
  .blend-name {
    font-family: "Josefin Sans", sans-serif; font-weight: 700;
    color: var(--paper); font-size: 30px; letter-spacing: 9px;
    padding-top: 6px;
  }
  .front-brand {
    position: absolute; top: 250px; left: 0; right: 0;
    display: flex; flex-direction: column; align-items: center; gap: 18px;
  }
  .brand-dot { width: 70px; height: 70px; border-radius: 50%; background: var(--red); }
  .brand-name {
    font-family: "Josefin Sans", sans-serif; font-weight: 700;
    color: var(--red); font-size: 40px; letter-spacing: 3px;
  }

  /* back */
  .web-band {
    position: absolute; top: 86px; left: 42px; width: 304px; height: 26px;
    background: var(--red); color: var(--paper);
    font-family: "Josefin Sans", sans-serif; font-weight: 700;
    font-size: 12px; letter-spacing: 4px;
    display: flex; align-items: center; justify-content: center; padding-top: 3px;
  }
  .story-title {
    position: absolute; top: 120px; left: 42px; width: 316px;
    font-family: "Josefin Sans", sans-serif; font-weight: 700;
    font-size: 28px; letter-spacing: 7.2px; color: var(--ink);
    border-bottom: 2px solid var(--ink); padding-bottom: 2px;
  }
  .story {
    position: absolute; top: 172px; left: 48px; width: 304px;
    color: var(--red); font-size: 6.6px; line-height: 1.45; text-align: center;
    display: flex; flex-direction: column; gap: 9px; font-weight: 500;
  }
  .address-row {
    position: absolute; top: 310px; left: 48px; width: 304px;
    display: flex; font-size: 7px; border-top: 1px solid var(--ink);
  }
  .address-row span { padding: 4px 6px; flex: 1; text-align: center; }
  .address-row .street { background: var(--grey-line); color: var(--paper); }
  .contact-line { position: absolute; top: 336px; left: 52px; font-size: 7px; }
  .label-box {
    position: absolute; left: 52px; border: 2px solid var(--red);
    font-size: 7px; text-align: center;
  }
  .label-box .label-head {
    background: var(--red); color: var(--paper);
    font-family: "Josefin Sans", sans-serif; font-weight: 700;
    font-size: 8px; padding: 4px 6px 2px; text-align: left;
  }
  .label-box .label-value { padding: 3px; letter-spacing: 1px; }
  .roasted { top: 368px; width: 214px; }
  .best-before { top: 414px; width: 140px; }
  .best-before .label-value { color: #777; }
  .caffeine {
    position: absolute; top: 456px; left: 52px;
    font-size: 5.6px; line-height: 2;
  }
  .back-brand {
    position: absolute; top: 420px; left: 222px;
    display: flex; align-items: center; gap: 8px;
  }
  .back-brand .brand-dot { width: 18px; height: 18px; background: var(--ink); }
  .back-brand .brand-name { color: var(--ink); font-size: 24px; letter-spacing: 1px; }
  .net-weight {
    position: absolute; top: 508px; left: 0; right: 0; text-align: center;
    font-family: "Josefin Sans", sans-serif; font-weight: 700;
    color: var(--red); font-size: 12px; letter-spacing: 4px;
  }
</style>
</head>
<body>
  <section class="bag-face bag-front">
    <div class="blend-band"><h1 class="blend-name">HOUSE BLEND</h1></div>
    <div class="front-brand">
      <div class="brand-dot"></div>
      <div class="brand-name">DELVANA</div>
    </div>
  </section>

  <section class="bag-face bag-back">
    <div class="web-band">WWW.DELVANACOFFEE.COM</div>
    <h2 class="story-title">HANDCRAFTED</h2>
    <div class="story">
      <p>In 2019 besloten Arne en Lotte de oude familietraditie nieuw leven in te blazen. Vijf generaties lang stond ons huis garant voor ambachtelijk gebrande koffie van hoge kwaliteit. Onze blends volgen het beproefde recept van de familie. Ons doel: u laten genieten van een lekkere kop koffie!</p>
      <p>En 2019, Arne et Lotte décident de continuer l'ancienne tradition familiale. Depuis cinq générations, notre maison garantit un café torréfié artisanalement et de grande qualité. Nos mélanges suivent la recette de nos ancêtres. Notre objectif : vous permettre de savourer une bonne tasse de café !</p>
      <p>In 2019 Arne and Lotte decided to revive the old family tradition. For five generations our house has stood for artisanally roasted premium coffee. All our blends are based on the old family recipes. Our main purpose is to let you enjoy a nice cup of coffee!</p>
    </div>
    <div class="address-row">
      <span>KOFFIE DELVANA</span>
      <span class="street">LINDEVELDSTRAAT 12</span>
      <span>9000 OUDEBEEK</span>
    </div>
    <p class="contact-line">INFO@KOFFIEDELVANA.BE – +32 00 11 22 33 – WWW.KOFFIEDELVANA.BE</p>
    <div class="label-box roasted">
      <div class="label-head">GEBRAND OP / TORREFIE LE / ROASTED ON</div>
      <div class="label-value">17/03/23</div>
    </div>
    <div class="label-box best-before">
      <div class="label-head">THT / DDM / BEST BEFORE</div>
      <div class="label-value">Consume within 12 months</div>
    </div>
    <div class="caffeine">
      <p>Cafeïnegehalte niet hoger dan 1,5%</p>
      <p>La teneur en caféine ne dépasse pas 1,5%</p>
      <p>Max. caffeine content 1,5%</p>
    </div>
    <div class="back-brand">
      <div class="brand-dot"></div>
      <div class="brand-name">DELVANA</div>
    </div>
    <p class="net-weight">250GR NETTO</p>
  </section>
</body>
</html>
```